Professional Website

We are looking for a new website for our Staffing Company. Attached is a document with all the details and pages needed along with some examples of others websites.

We want a professional Look and feel around the same color theme as the attached Vivid Vision.

We currently host our site on Pagecraft.io. If the winning designer can also add to Pagecraft, that is a plus.

```html
<!DOCTYPE html>
<html lang="en">
<head>
<meta charset="utf-8">
<title>Crewline Inc – Website Layouts</title>
<link rel="stylesheet" href="https://fonts.googleapis.com/css2?family=Montserrat:wght@500;600;700&family=Roboto:wght@400;500;700&display=swap">
<style>
:root{
  --canvas:#e8e8e8;
  --blue:#2436c0;
  --ink:#222326;
  --grey-text:#6b6e75;
  --white:#ffffff;
}
*{box-sizing:border-box;margin:0;padding:0}
html,body{width:1052px;height:1200px;overflow:hidden;background:var(--canvas)}
body{position:relative;font-family:"Roboto",Arial,sans-serif;color:var(--ink)}
.page{position:absolute;width:421px;background:var(--white);overflow:hidden;box-shadow:0 2px 8px rgba(0,0,0,.08)}
.page--home{left:75px;top:72px;height:1055px}
.page--landing{left:556px;top:72px;height:551px}
.abs{position:absolute}

.topbar{position:absolute;left:0;top:0;width:421px;height:15px;background:var(--blue);color:var(--white);font-size:4.6px;display:flex;align-items:center;padding:0 39px}
.topbar__item{margin-right:14px;display:flex;align-items:center;gap:3px}
.topbar__social{margin-left:auto;display:flex;gap:5px}
.topbar__social span{width:4px;height:4px;border-radius:50%;background:var(--white)}
.icon{width:5px;height:5px}

.header{position:absolute;left:0;top:15px;width:421px;height:33px;background:var(--white)}
.brand{position:absolute;left:39px;top:9px;font-family:"Roboto",sans-serif;font-weight:700;font-size:15px;color:var(--blue);line-height:1}
.login{position:absolute;top:8px;width:57px;height:15px;display:flex;align-items:center;justify-content:center;font-size:4.6px;font-weight:700;color:var(--white);background:var(--blue);text-transform:uppercase;white-space:nowrap}
.login--dark{background:var(--ink)}

.btn{display:inline-flex;align-items:center;gap:2px;background:var(--blue);color:var(--white);font-weight:700;font-size:4.4px;text-transform:uppercase;padding:0 9px;height:14px}
.cta-bar{position:absolute;display:flex;align-items:center;justify-content:center;background:var(--blue);color:var(--white);font-family:"Montserrat",sans-serif;font-weight:600;font-size:8.6px;text-transform:uppercase}
.photo{position:absolute}

.hero{position:absolute;left:0;top:48px;width:421px;height:252px}
.hero__box{position:absolute;left:222px;top:49px;width:159px;height:90px;background:rgba(70,72,78,.82);color:var(--white);text-align:center;padding-top:9px}
.hero__title{font-family:"Montserrat",sans-serif;font-weight:600;font-size:18.5px;letter-spacing:.3px;white-space:nowrap}
.hero__text{font-size:4.4px;line-height:9px;margin-top:4px}
.hero__box .btn{margin-top:6px}
.scroll{position:absolute;left:250px;top:192px;font-size:3.4px;color:var(--white);text-transform:uppercase;width:50px;text-align:center}
.scroll__dot{position:absolute;left:268px;top:211px;width:15px;height:15px;border-radius:50%;background:#e9e9ea;display:flex;align-items:center;justify-content:center}

.welcome{position:absolute;left:0;width:421px;text-align:center}
.welcome__kicker{font-family:"Montserrat",sans-serif;font-weight:600}
.welcome__title{font-family:"Montserrat",sans-serif;font-weight:600;white-space:nowrap}
.welcome__text{font-size:4.5px;line-height:9px}
.welcome--blue{top:514px;height:254px;color:var(--white);background:linear-gradient(135deg,#2a3ec4,#1f30b4 60%,#2b3ab8)}
.welcome--blue .content{position:absolute;left:0;top:72px;width:100%}
.welcome--blue .welcome__kicker{font-size:7.5px}
.welcome--blue .welcome__title{font-size:18px;margin-top:1px}
.welcome--blue .welcome__text{margin-top:9px;padding:0 60px}
.welcome--blue .btn{margin-top:8px;background:#2739c8}
.welcome--light{top:265px;height:200px;background:linear-gradient(180deg,#f3f4f6,#eceef1)}
.welcome--light .content{position:absolute;left:0;top:30px;width:100%}
.welcome--light .welcome__kicker{font-size:4.8px;color:var(--blue);letter-spacing:2px}
.welcome--light .welcome__title{font-size:14px;margin-top:2px;color:var(--ink)}
.rule{width:35px;height:1px;background:var(--blue);margin:5px auto 8px}
.welcome--light .welcome__text{color:var(--grey-text);padding:0 60px}
.welcome--light .btn{margin-top:8px}

.contact{position:absolute;left:0;top:775px;width:421px;height:135px}
.contact__map{position:absolute;left:75px;top:6px;width:270px;height:118px;background:radial-gradient(ellipse at center,#f2f2f3 0%,#ffffff 70%)}
.contact__title{position:absolute;left:0;top:5px;width:100%;text-align:center;font-family:"Montserrat",sans-serif;font-weight:600;font-size:13px}
.field{position:absolute;border:.6px solid #d6d7da;background:var(--white);font-size:4.6px;color:#55585e;padding:7px}
.field--active{border-color:#3d4cc9}
.submit{position:absolute;left:182px;top:104px;width:57px;height:15px;justify-content:center;padding:0}

.footer{position:absolute;left:0;width:421px;background:linear-gradient(160deg,#1d2230,#101218 55%,#1b1f28)}
.footer--home{top:905px;height:150px}
.footer--landing{top:408px;height:143px}
.footer svg{position:absolute;left:0;top:0}
.footer__inner{position:absolute;left:0;width:100%;text-align:center;color:var(--white)}
.footer__brand{font-family:"Roboto",sans-serif;font-weight:700;font-size:15px;line-height:1}
.footer__areas{font-weight:700;font-size:5.8px;text-decoration:underline;margin-top:12px}
.footer__cities{font-weight:700;font-size:4.8px;margin-top:9px}
.footer__cities span{margin:0 7px}
.footer__copy{font-size:5.2px;margin-top:14px}

.band{position:absolute;left:2px;top:48px;width:417px;height:5px;border-radius:2.5px;background:var(--blue)}
</style>
</head>
<body>

<section class="page page--home" aria-label="Home page layout">
  <div class="topbar">
    <span class="topbar__item"><svg class="icon" viewBox="0 0 10 10"><rect x="1" y="2" width="8" height="6" fill="none" stroke="#fff" stroke-width="1"/><path d="M1 2l4 3.5L9 2" fill="none" stroke="#fff" stroke-width="1"/></svg>hello@crewline.example</span>
    <span class="topbar__item"><svg class="icon" viewBox="0 0 10 10"><path d="M2 1l2 .5.5 2-1 1a5 5 0 0 0 2 2l1-1 2 .5.5 2C6 9 1 4 2 1z" fill="#fff"/></svg>Our Hotline : 08-555-0140</span>
    <span class="topbar__social"><span></span><span></span><span></span><span></span><span></span></span>
  </div>
  <header class="header">
    <div class="brand">Crewline</div>
    <a class="login" style="left:198px">Employee Login</a>
    <a class="login login--dark" style="left:261px">Pay Card Login</a>
    <a class="login" style="left:325px">Partner Bank Login</a>
  </header>

  <div class="hero">
    <div class="photo" role="img" aria-label="Photo of a smiling business team in suits standing in a bright office" style="left:0;top:0;width:421px;height:252px;background:linear-gradient(110deg,#3c4656 0%,#8a919c 35%,#d9dbde 55%,#7c828c 80%,#4a505a 100%)"></div>
    <div class="hero__box">
      <div class="hero__title">CREWLINE INC</div>
      <p class="hero__text">To change the way temporary staffing agencies fill orders.<br>We only work with the best companies and best employees.</p>
      <span class="btn">Learn More <svg class="icon" viewBox="0 0 10 10"><circle cx="5" cy="5" r="4.5" fill="#fff"/><path d="M4 3l2 2-2 2" stroke="#2436c0" fill="none" stroke-width="1.3"/></svg></span>
    </div>
    <svg class="abs" style="left:0;top:0" width="421" height="252" viewBox="0 0 421 252">
      <polygon points="277,220 421,201 421,236" fill="#2436c0"/>
      <polygon points="0,252 277,220 421,236 421,252" fill="#fff"/>
    </svg>
    <div class="scroll">Scroll down</div>
    <div class="scroll__dot"><svg width="5" height="5" viewBox="0 0 10 10"><path d="M2 2l3 3 3-3M2 5l3 3 3-3" stroke="#555" fill="none" stroke-width="1.2"/></svg></div>
  </div>

  <div class="photo" role="img" aria-label="Photo of colleagues giving a high five in an office, one seated in a wheelchair" style="left:39px;top:312px;width:166px;height:156px;background:linear-gradient(135deg,#8f8a84,#c9c6c1 50%,#5b6472)"></div>
  <div class="cta-bar" style="left:39px;top:477px;width:167px;height:24px">I'm looking for a job</div>
  <div class="cta-bar" style="left:215px;top:313px;width:166px;height:23px">I need employees</div>
  <div class="photo" role="img" aria-label="Photo of a smiling team gathered around a laptop at a meeting table" style="left:215px;top:345px;width:166px;height:157px;background:linear-gradient(160deg,#a7b1b8,#6f7c84 45%,#b9875e 75%,#e6e2dd)"></div>

  <section class="welcome welcome--blue">
    <svg class="abs" style="left:0;top:0" width="421" height="254" viewBox="0 0 421 254">
      <polygon points="270,35 421,17 421,52" fill="#25272b"/>
      <polygon points="0,0 421,0 421,17 270,35" fill="#fff"/>
      <polygon points="280,218 421,200 421,237" fill="#25272b"/>
      <polygon points="0,254 280,218 421,237 421,254" fill="#fff"/>
    </svg>
    <div class="content">
      <div class="welcome__kicker">WELCOME TO</div>
      <div class="welcome__title">CREWLINE INC</div>
      <p class="welcome__text">Greatest part of our daily job is that we are constantly bringing people together. Our Clients come to us in search of the perfect candidate and the job hunters approach us when they are in need of a job or looking for their next exciting role.</p>
      <p class="welcome__text" style="margin-top:9px">Being able to work with and connect the two is incredibly satisfying. Not to mention that in today's current job market, employers are fighting for the top talent. This makes our employees and partners grateful for the help in finding it!</p>
      <span class="btn">Learn More <svg class="icon" viewBox="0 0 10 10"><circle cx="5" cy="5" r="4.5" fill="#fff"/><path d="M4 3l2 2-2 2" stroke="#2436c0" fill="none" stroke-width="1.3"/></svg></span>
    </div>
  </section>

  <section class="contact">
    <div class="contact__map" role="img" aria-label="Faint dotted world map behind the contact form"></div>
    <h2 class="contact__title">GET IN TOUCH</h2>
    <div class="field field--active" style="left:64px;top:28px;width:94px;height:19px">Name*</div>
    <div class="field" style="left:163px;top:28px;width:94px;height:19px">Email address*</div>
    <div class="field" style="left:262px;top:28px;width:94px;height:19px">Phone*</div>
    <div class="field" style="left:64px;top:53px;width:292px;height:45px">Message*</div>
    <span class="btn submit">Submit Now</span>
  </section>

  <footer class="footer footer--home">
    <svg width="421" height="150" viewBox="0 0 421 150">
      <polygon points="0,0 421,0 145,35 0,18" fill="#fff"/>
      <polygon points="0,18 145,35 0,53" fill="#2436c0"/>
    </svg>
    <div class="footer__inner" style="top:62px">
      <div class="footer__brand">Crewline</div>
      <div class="footer__areas">AREAS WE SERVICE</div>
      <div class="footer__cities">CEDAR POINT<span>/</span>FAIRBROOK<span>/</span>MILLHAVEN</div>
      <div class="footer__copy">© 2022 Crewline Inc | All Rights Reserved | Terms and Conditions</div>
    </div>
  </footer>
</section>

<section class="page page--landing" aria-label="Landing page layout">
  <div class="topbar">
    <span class="topbar__item"><svg class="icon" viewBox="0 0 10 10"><rect x="1" y="2" width="8" height="6" fill="none" stroke="#fff" stroke-width="1"/><path d="M1 2l4 3.5L9 2" fill="none" stroke="#fff" stroke-width="1"/></svg>hello@crewline.example</span>
    <span class="topbar__item"><svg class="icon" viewBox="0 0 10 10"><path d="M2 1l2 .5.5 2-1 1a5 5 0 0 0 2 2l1-1 2 .5.5 2C6 9 1 4 2 1z" fill="#fff"/></svg>Our Hotline : 08-555-0140</span>
    <span class="topbar__social"><span></span><span></span><span></span><span></span><span></span></span>
  </div>
  <header class="header">
    <div class="brand">Crewline</div>
    <a class="login" style="left:198px">Employee Login</a>
    <a class="login login--dark" style="left:261px">Pay Card Login</a>
    <a class="login" style="left:325px">Partner Bank Login</a>
  </header>

  <div class="band"></div>

  <div class="photo" role="img" aria-label="Photo of a diverse team stacking hands together in celebration" style="left:11px;top:60px;width:194px;height:196px;background:linear-gradient(150deg,#c9b39a,#e3ded6 35%,#6c7380 70%,#3a4150)"></div>
  <div class="cta-bar" style="left:19px;top:231px;width:178px;height:18px">I'm looking for a job</div>
  <div class="photo" role="img" aria-label="Photo of a confident group of professionals standing with arms crossed" style="left:215px;top:60px;width:194px;height:196px;background:linear-gradient(160deg,#dfe2e5,#b7bcc2 40%,#7d8593 75%,#59606d)"></div>
  <div class="cta-bar" style="left:223px;top:231px;width:178px;height:18px">I need employees</div>

  <section class="welcome welcome--light">
    <div class="content">
      <div class="welcome__kicker">WELCOME TO</div>
      <div class="welcome__title">CREWLINE INC</div>
      <div class="rule"></div>
      <p class="welcome__text">Greatest part of our daily job is that we are constantly bringing people together. Our Clients come to us in search of the perfect candidate and the job hunters approach us when they are in need of a job or looking for their next exciting role.</p>
      <p class="welcome__text" style="margin-top:9px">Being able to work with and connect the two is incredibly satisfying. Not to mention that in today's current job market, employers are fighting for the top talent. This makes our employees and partners grateful for the help in finding it!</p>
      <span class="btn">Learn More <svg class="icon" viewBox="0 0 10 10"><circle cx="5" cy="5" r="4.5" fill="#fff"/><path d="M4 3l2 2-2 2" stroke="#2436c0" fill="none" stroke-width="1.3"/></svg></span>
    </div>
  </section>

  <footer class="footer footer--landing">
    <svg width="421" height="143" viewBox="0 0 421 143">
      <polygon points="0,0 421,0 145,34 0,16" fill="#eceef1"/>
      <polygon points="0,16 145,34 0,52" fill="#2436c0"/>
    </svg>
    <div class="footer__inner" style="top:58px">
      <div class="footer__brand">Crewline</div>
      <div class="footer__areas">AREAS WE SERVICE</div>
      <div class="footer__cities">CEDAR POINT<span>/</span>FAIRBROOK<span>/</span>MILLHAVEN</div>
      <div class="footer__copy">© 2022 Crewline Inc | All Rights Reserved | Terms and Conditions</div>
    </div>
  </footer>
</section>

</body>
</html>
```